Biotech company website design

We are looking for innovative design of our upcoming website. We are a small biotechnology company in Europe dealing with life science products and services.
Updates

Please incorporate the following top level links:
ABOUT US, PRODUCTS, SERVICES, SUPPLIERS, NEWS AND PROMOS, CONTACT US

Target Market(s)

Science people, hospitals, universities ....

Industry/Entity Type

It Company

Requirements
Must have
• Must incorporate our current logo (its color toning)

```html
<!DOCTYPE html>
<html lang="en">
<head>
<meta charset="utf-8">
<title>VerdaBio Labs</title>
<link rel="stylesheet" href="https://fonts.googleapis.com/css2?family=Open+Sans:wght@400;600;700&family=Noto+Serif&display=swap">
<style>
:root{
  --green:#7cb52a;
  --green-dark:#5e9219;
  --green-pale:#dfe9cf;
  --green-band:#c9dcae;
  --ink:#3e3e3e;
  --text:#6a6a6a;
  --muted:#8c8c8c;
  --rule:#cfcfcf;
  --page:#f3f3f1;
  --footer:#e2e2e0;
  --charcoal:#5a5a5a;
  --white:#ffffff;
}
*{box-sizing:border-box;margin:0;padding:0}
html,body{width:777px;height:1200px;overflow:hidden}
body{position:relative;background:var(--page);font-family:"Open Sans",Arial,sans-serif;color:var(--text);font-size:8px;line-height:1.35}
.abs{position:absolute}
.band{position:absolute}
.band-a{left:0;top:349px;width:36px;height:131px;background:var(--green-band)}
.band-b{left:0;top:480px;width:53px;height:153px;background:var(--green-pale)}
.band-c{left:751px;top:689px;width:26px;height:137px;background:var(--green-pale)}
.band-d{left:732px;top:833px;width:45px;height:140px;background:#c7d1bb}

.logo{left:87px;top:22px;display:flex;align-items:center;gap:6px}
.logo-mark{width:18px;height:18px;background:var(--green)}
.logo-name{font-size:16px;font-weight:600;color:var(--ink)}
.account-links{right:81px;top:12px;font-size:7.5px;color:var(--ink)}
.tool-btn{top:42px;width:22px;height:22px;border-radius:50%;background:var(--green);border:2px solid var(--white);box-shadow:0 1px 3px rgba(0,0,0,.3)}
.search{left:580px;top:42px;width:121px;height:24px;border-radius:12px;background:var(--white);box-shadow:0 1px 3px rgba(0,0,0,.25)}
.search-field{left:618px;top:49px;width:76px;height:10px;border-radius:5px;background:#dcdcdc}

.nav a{position:absolute;font-size:8px;font-weight:600;color:var(--green-dark);text-decoration:none;transform:translateX(-50%);top:72px}
.nav .dot{position:absolute;width:11px;height:11px;border-radius:50%;background:#4a4a4a;top:84px;transform:translateX(-50%)}

.hero{left:76px;top:91px;width:621px;height:258px;border-radius:8px;overflow:hidden;background:linear-gradient(90deg,#6a5c4c 0%,#9a8a78 35%,#c9c5bd 60%,#e9e8e6 100%)}
.hero-arrow{top:189px;width:22px;height:40px;background:var(--green);border-radius:4px}
.login{left:68px;top:240px;width:228px;height:80px;background:rgba(40,40,40,.8);border-radius:0 0 4px 4px}
.login span{position:absolute;left:16px;color:var(--white);font-size:8.5px}
.login .line{position:absolute;left:12px;width:190px;height:1px;background:rgba(255,255,255,.25)}
.login-go{left:278px;top:260px;width:34px;height:34px;border-radius:50%;background:#333;border:3px solid #555}
.slider-dots{left:360px;top:332px;display:flex;gap:4px}
.slider-dots i{width:7px;height:7px;border-radius:50%;background:var(--white)}
.slider-dots i:first-child{background:var(--green)}

.section-title{position:absolute;font-size:12.5px;color:var(--ink)}
.section-title::after{content:"";position:absolute;left:0;bottom:-4px;width:20px;height:2px;background:var(--green)}
.rule{position:absolute;height:1px;background:var(--rule)}
.para{position:absolute;font-size:7px;color:var(--text);line-height:1.42}
.welcome-text{font-size:6.8px;line-height:1.38}
.btn{position:absolute;height:12px;background:#e7e7e7;border:1px solid #cfcfcf;font-size:6.5px;color:var(--ink);text-align:center;line-height:10px;border-left:3px solid var(--green);border-right:3px solid var(--green)}

.ads{left:496px;top:373px;width:201px;height:267px;background:var(--white);border:1px solid #dcdcdc;border-radius:10px}
.ads-head{left:508px;top:381px;font-size:6.5px;color:var(--ink)}
.ads-head b{color:var(--green-dark);font-weight:600}
.ads-inner{left:508px;top:425px;width:180px;height:198px;background:#ececec;border-radius:6px}
.ad-img{width:70px;height:52px;border-radius:6px}
.ad-title{font-size:7px;font-weight:600;color:var(--green-dark)}
.ad-text{font-size:5.8px;color:var(--muted);line-height:1.3}
.ad-dot{width:6px;height:6px;border-radius:50%;background:var(--green)}
.ads-more{left:514px;top:626px;font-size:6.5px;color:var(--green-dark);font-weight:600}

.flask{position:absolute;width:12px;height:14px}
.news-title{position:absolute;font-size:7.5px;color:var(--green-dark);font-weight:600;line-height:1.3}
.pager{position:absolute;top:518px;width:10px;height:10px;border:1px solid #aaa;background:#eee}

.card-img{position:absolute;top:680px;width:190px;height:107px;border-radius:8px}
.card-title{position:absolute;top:797px;font-size:8px;color:var(--green-dark);font-weight:600;line-height:1.25}

.comments{left:76px;top:896px;width:371px;height:128px;background:var(--charcoal);border-radius:8px}
.comments-tail{left:335px;top:1022px}
.bubble{position:absolute;top:913px;width:104px;height:50px;background:var(--white);border-radius:7px}
.avatar{position:absolute;top:919px;width:38px;height:38px;border-radius:4px;background:linear-gradient(#b8b2a8,#7d766c)}
.bubble-name{position:absolute;top:929px;font-size:6px;color:var(--ink);line-height:1.2}
.bubble-name b{font-weight:600;color:var(--green-dark)}
.bubble-text{position:absolute;top:986px;width:104px;font-size:5.8px;color:var(--white);line-height:1.35}

.video{left:495px;top:896px;width:202px;height:131px;background:linear-gradient(180deg,#d8d6d2,#a9a6a0);border-radius:2px}
.video-bar{left:495px;top:1013px;width:202px;height:14px;background:#e9e9e9;border-top:1px solid #ccc}
.video-tag{left:607px;top:896px;width:90px;height:9px;background:#222;color:var(--white);font-size:5px;line-height:9px;text-align:center}

.footer{left:0;top:1053px;width:777px;height:147px;background:var(--footer);border-top:1px solid #d0d0d0}
.f-title{position:absolute;top:1066px;font-family:"Noto Serif",Georgia,serif;font-size:10.5px;color:var(--green-dark)}
.f-div{position:absolute;top:1068px;width:1px;height:122px;background:#c6c6c6}
.f-list{position:absolute;list-style:none;font-size:7px;color:var(--ink)}
.f-list li{height:15.2px;display:flex;align-items:center;gap:6px}
.f-list li::before{content:"";width:5px;height:5px;background:var(--green)}
.f-contact{position:absolute;font-size:6.5px;color:var(--ink);line-height:1.3}
.social{position:absolute;left:569px;font-size:7.5px;color:var(--ink);display:flex;align-items:center;gap:8px}
.social i{width:16px;height:16px;background:#777;border-radius:2px}
.signup{left:80px;top:1110px;width:170px;height:22px;background:var(--white);border:1px solid #c9c9c9;font-size:7px;color:var(--muted);font-style:italic;padding:6px 6px}
.signup-go{left:240px;top:1109px;width:32px;height:24px;background:var(--green);border-radius:2px}
</style>
</head>
<body>

<div class="band band-a"></div>
<div class="band band-b"></div>
<div class="band band-c"></div>
<div class="band band-d"></div>

<!-- Header -->
<div class="abs logo"><span class="logo-mark"></span><span class="logo-name">VerdaBio Labs</span></div>
<div class="abs account-links">My Account | My Cart | My Orders | New Customer</div>
<div class="abs tool-btn" style="left:520px"></div>
<div class="abs tool-btn" style="left:553px"></div>
<div class="abs search"></div>
<div class="abs tool-btn" style="left:584px;top:43px;width:20px;height:20px"></div>
<div class="abs search-field"></div>
<svg class="abs" style="left:522px;top:44px" width="18" height="18" viewBox="0 0 18 18"><path d="M4 10 L9 5 L14 10 M6 9 V14 H12 V9" fill="none" stroke="#fff" stroke-width="1.6"/></svg>
<svg class="abs" style="left:555px;top:44px" width="18" height="18" viewBox="0 0 18 18"><text x="9" y="13" text-anchor="middle" font-family="Open Sans,sans-serif" font-weight="700" font-size="11" fill="#fff">?</text></svg>
<svg class="abs" style="left:587px;top:46px" width="14" height="14" viewBox="0 0 14 14"><circle cx="6" cy="6" r="3.5" fill="none" stroke="#fff" stroke-width="1.5"/><path d="M8.5 8.5 L12 12" stroke="#fff" stroke-width="1.6"/></svg>

<nav class="nav">
  <a href="#" style="left:112px">HOME</a><span class="dot" style="left:112px"></span>
  <a href="#" style="left:195px;top:65px">ABOUT US</a><span class="dot" style="left:195px;top:80px;width:13px;height:13px"></span>
  <a href="#" style="left:280px">PRODUCTS</a><span class="dot" style="left:280px"></span>
  <a href="#" style="left:365px">SERVICES</a><span class="dot" style="left:365px"></span>
  <a href="#" style="left:449px">SUPPLIER</a><span class="dot" style="left:449px"></span>
  <a href="#" style="left:549px">NEWS &amp; PROMOS</a><span class="dot" style="left:549px"></span>
  <a href="#" style="left:655px">CONTACT US</a><span class="dot" style="left:655px"></span>
</nav>

<!-- Hero -->
<div class="abs hero" role="img" aria-label="Smiling scientist in a lab coat in front of a laboratory"></div>
<div class="abs hero-arrow" style="left:71px"></div>
<div class="abs hero-arrow" style="left:679px"></div>
<svg class="abs" style="left:75px;top:202px" width="14" height="14" viewBox="0 0 14 14"><path d="M9 2 L4 7 L9 12" fill="none" stroke="#fff" stroke-width="2"/></svg>
<svg class="abs" style="left:683px;top:202px" width="14" height="14" viewBox="0 0 14 14"><path d="M5 2 L10 7 L5 12" fill="none" stroke="#fff" stroke-width="2"/></svg>
<div class="abs login">
  <span style="top:17px">username</span><i class="line" style="top:33px"></i>
  <span style="top:48px">password</span><i class="line" style="top:64px"></i>
</div>
<div class="abs login-go"></div>
<svg class="abs" style="left:290px;top:271px" width="12" height="12" viewBox="0 0 12 12"><path d="M3 1 L10 6 L3 11 Z" fill="#ddd"/></svg>
<div class="abs slider-dots"><i></i><i></i><i></i><i></i></div>

<!-- Welcome -->
<h1 class="section-title" style="left:76px;top:368px;font-weight:400">Welcome To Our Company!</h1>
<div class="rule" style="left:76px;top:390px;width:364px"></div>
<p class="para welcome-text" style="left:76px;top:396px;width:364px">Lorem Ipsum is simply dummy text of the printing and typesetting industry. Lorem Ipsum has been the industry's standard dummy text ever since the 1500s, when an unknown printer took a galley of type and scrambled it to make a type specimen book. It has survived not only five centuries, but also the leap into electronic typesetting, remaining essentially unchanged. It was popularised in the 1960s with the release of Typeline sheets containing Lorem Ipsum passages, and more recently with desktop publishing software like PageForge Studio including versions of Lorem Ipsum. It is a long established fact that a reader will be distracted by the readable content of a page when looking at its layout. The point of using Lorem Ipsum is that it has a more-or-less normal distribution of letters, as opposed to using 'Content here, content here', making it look like readable English.</p>
<div class="btn" style="left:379px;top:481px;width:61px">READ MORE</div>

<!-- Ads -->
<div class="abs ads"></div>
<div class="abs ads-head"><b>List Of Advertisement</b><br>Lorem Ipsum is simply?<br>Contrary to popular belief?</div>
<div class="rule" style="left:508px;top:415px;width:178px"></div>
<div class="abs ads-inner"></div>
<div class="abs" style="left:513px;top:431px;display:flex;flex-direction:column;gap:12px">
  <div style="display:flex;gap:8px"><div class="ad-img" role="img" aria-label="Coloured test tubes in a rack" style="background:linear-gradient(135deg,#8fb6c9,#c64b4b)"></div><div style="width:90px"><div class="ad-title">Lorem ipsum dolor sit</div><div class="ad-text">Sed ut perspiciatis unde omnis iste natus error sit voluptatem accusantium doloremque</div><div class="ad-dot" style="margin:2px 0 0 78px"></div></div></div>
  <div style="display:flex;gap:8px"><div class="ad-img" role="img" aria-label="Gloved hand holding a sample vial" style="background:linear-gradient(135deg,#e8ecef,#9fb0bd)"></div><div style="width:90px"><div class="ad-title">Lorem ipsum dolor sit</div><div class="ad-text">Sed ut perspiciatis unde omnis iste natus error sit voluptatem accusantium doloremque</div><div class="ad-dot" style="margin:2px 0 0 78px"></div></div></div>
  <div style="display:flex;gap:8px"><div class="ad-img" role="img" aria-label="Gloved hand holding a green test tube" style="background:linear-gradient(135deg,#f0ecea,#d9a5a5 60%,#7cb52a)"></div><div style="width:90px"><div class="ad-title">Lorem ipsum dolor sit</div><div class="ad-text">Sed ut perspiciatis unde omnis iste natus error sit voluptatem accusantium doloremque</div><div class="ad-dot" style="margin:2px 0 0 78px"></div></div></div>
</div>
<div class="abs ads-more">View All Ads &#187;</div>

<!-- Latest News -->
<h2 class="section-title" style="left:76px;top:513px;font-weight:400">Latest News!</h2>
<div class="rule" style="left:76px;top:535px;width:364px"></div>
<div class="pager" style="left:414px"></div><div class="pager" style="left:427px"></div>
<svg class="abs" style="left:414px;top:518px" width="24" height="10" viewBox="0 0 24 10"><path d="M6 2 L3 5 L6 8 M17 2 L20 5 L17 8" fill="none" stroke="#555" stroke-width="1.2"/></svg>
<svg class="flask" style="left:80px;top:543px" viewBox="0 0 12 14"><path d="M4 0 H8 V4 L12 13 H0 L4 4 Z" fill="#7cb52a"/><path d="M2 10 H10 L12 13 H0 Z" fill="#5e9219"/></svg>
<div class="news-title" style="left:97px;top:541px;width:150px">The standard Lorem Ipsum<br>passage, used since the 1500s</div>
<div class="rule" style="left:80px;top:565px;width:176px"></div>
<p class="para" style="left:80px;top:569px;width:180px">Lorem ipsum dolor sit amet, consectetur adipisicing elit, sed do eiusmod tempor incididunt ut labore et dolore magna aliqua. Ut enim ad minim veniam, quis nostrud exercitation ullamco laboris nisi ut aliquip ex ea commodo consequat. Duis aute irure dolor in</p>
<div class="rule" style="left:273px;top:540px;width:1px;height:88px"></div>
<svg class="flask" style="left:284px;top:543px" viewBox="0 0 12 14"><path d="M4 0 H8 V4 L12 13 H0 L4 4 Z" fill="#7cb52a"/><path d="M2 10 H10 L12 13 H0 Z" fill="#5e9219"/></svg>
<div class="news-title" style="left:302px;top:541px;width:140px">The standard Lorem Ipsum<br>passage, used since the 1500s</div>
<div class="rule" style="left:284px;top:565px;width:156px"></div>
<p class="para" style="left:284px;top:569px;width:158px">Lorem ipsum dolor sit amet, consectetur adipisicing elit, sed do eiusmod tempor incididunt ut labore et dolore magna aliqua. Ut enim ad minim veniam, quis nostrud exercitation ullamco laboris nisi ut aliquip ex ea commodo consequat. Duis aute irure dolor in</p>

<!-- Selected News -->
<h2 class="section-title" style="left:76px;top:649px;font-weight:400">Selected News</h2>
<div class="rule" style="left:76px;top:668px;width:621px"></div>
<div class="card-img" style="left:79px;background:radial-gradient(circle at 45% 45%,#d5d5d5,#6e6e6e 45%,#1f1f1f 80%)" role="img" aria-label="Close-up of a microscope objective lens"></div>
<div class="card-img" style="left:293px;background:linear-gradient(180deg,#e9f1f6 0%,#cfe0ea 60%,#7aa63a 80%,#6b4d2d 100%)" role="img" aria-label="Young green seedling growing from soil"></div>
<div class="card-img" style="left:507px;background:linear-gradient(135deg,#2e3b5e,#5a6f99 60%,#b48a6e)" role="img" aria-label="Scientist looking thoughtful"></div>
<svg class="flask" style="left:80px;top:797px" viewBox="0 0 12 14"><path d="M4 0 H8 V4 L12 13 H0 L4 4 Z" fill="#7cb52a"/></svg>
<div class="card-title" style="left:104px;top:798px">Neque porro quisquam est</div>
<svg class="flask" style="left:296px;top:797px" viewBox="0 0 12 14"><path d="M4 0 H8 V4 L12 13 H0 L4 4 Z" fill="#7cb52a"/></svg>
<div class="card-title" style="left:320px;top:792px;width:170px">dolorem ipsum quia dolor sit amet consectetur, adipisci velit</div>
<svg class="flask" style="left:510px;top:797px" viewBox="0 0 12 14"><path d="M4 0 H8 V4 L12 13 H0 L4 4 Z" fill="#7cb52a"/></svg>
<div class="card-title" style="left:534px;top:798px">Lorem ipsum dolor sit</div>
<div class="rule" style="left:79px;top:815px;width:190px"></div>
<div class="rule" style="left:293px;top:815px;width:190px"></div>
<div class="rule" style="left:507px;top:815px;width:190px"></div>
<p class="para" style="left:80px;top:821px;width:190px">Lorem Ipsum is simply dummy text of the printing and typesetting industry. Lorem Ipsum has been the industry's standard ...</p>
<p class="para" style="left:295px;top:821px;width:190px">Lorem Ipsum is simply dummy text of the printing and typesetting industry. Lorem Ipsum has been the industry's standard ...</p>
<p class="para" style="left:509px;top:821px;width:190px">Lorem Ipsum is simply dummy text of the printing and typesetting industry. Lorem Ipsum has been the industry's standard ...</p>

<!-- Recent Comments -->
<h2 class="section-title" style="left:76px;top:867px;font-weight:400">Recent Comments</h2>
<div class="rule" style="left:76px;top:886px;width:371px"></div>
<div class="abs comments"></div>
<svg class="abs comments-tail" width="16" height="16" viewBox="0 0 16 16"><path d="M0 0 H16 L8 14 Z" fill="#5a5a5a"/></svg>
<div class="bubble" style="left:84px"></div>
<div class="bubble" style="left:207px"></div>
<div class="bubble" style="left:329px"></div>
<div class="avatar" style="left:89px" role="img" aria-label="Commenter portrait"></div>
<div class="avatar" style="left:212px" role="img" aria-label="Commenter portrait"></div>
<div class="avatar" style="left:334px" role="img" aria-label="Commenter portrait"></div>
<div class="bubble-name" style="left:132px"><b>Mira Holt</b><br>- General Manager</div>
<div class="bubble-name" style="left:255px"><b>Mira Holt</b><br>- General Manager</div>
<div class="bubble-name" style="left:377px"><b>Mira Holt</b><br>- General Manager</div>
<p class="bubble-text" style="left:84px">consectetur adipisicing elit, sed do eiusmod tempor incididunt ut labore et dolore magna aliqua</p>
<p class="bubble-text" style="left:207px">consectetur adipisicing elit, sed do eiusmod tempor incididunt ut labore et dolore magna aliqua</p>
<p class="bubble-text" style="left:329px">consectetur adipisicing elit, sed do eiusmod tempor incididunt ut labore et dolore magna aliqua</p>

<!-- Video -->
<h2 class="section-title" style="left:495px;top:867px;font-weight:400">Our Video</h2>
<div class="rule" style="left:495px;top:886px;width:202px"></div>
<div class="abs video" role="img" aria-label="Video still of two presenters standing side by side"></div>
<div class="abs video-tag">ROLLOVER FOR MORE VIDEOS</div>
<svg class="abs" style="left:578px;top:936px" width="34" height="26" viewBox="0 0 34 26"><rect width="34" height="26" rx="4" fill="rgba(0,0,0,.55)"/><path d="M13 7 L23 13 L13 19 Z" fill="#fff"/></svg>
<div class="abs" style="left:570px;top:968px;font-size:9px;color:#fff;font-weight:600">Click for Sound</div>
<div class="abs video-bar"></div>
<svg class="abs" style="left:498px;top:1016px" width="196" height="9" viewBox="0 0 196 9"><path d="M1 1 L7 4.5 L1 8 Z" fill="#c0302a"/><rect x="12" y="2" width="6" height="5" fill="#777"/><text x="36" y="7" font-family="Open Sans,sans-serif" font-size="6" fill="#555">0:03 / 1:00</text><rect x="70" y="4" width="90" height="1.5" fill="#bbb"/><text x="164" y="7" font-family="Open Sans,sans-serif" font-size="6" fill="#555">360p</text><rect x="186" y="2" width="6" height="5" fill="none" stroke="#777"/></svg>

<!-- Footer -->
<footer class="abs footer"></footer>
<div class="f-title" style="left:80px">Get Latest News and Exclusive Offers</div>
<p class="para" style="left:80px;top:1081px;width:200px;color:var(--ink)">Lorem ipsum dolor sit amet, consectetur adipisicing elit, sed do eiusmod tempo</p>
<div class="abs signup">Enter Your E-mail Address</div>
<div class="abs signup-go"></div>
<svg class="abs" style="left:250px;top:1115px" width="12" height="12" viewBox="0 0 12 12"><path d="M3 1 L10 6 L3 11 Z" fill="#fff"/></svg>

<div class="f-div" style="left:291px"></div>
<div class="f-title" style="left:311px">Quick Links</div>
<ul class="f-list" style="left:311px;top:1082px">
  <li>Home</li><li>About Us</li><li>Products</li><li style="color:var(--green-dark)">Services</li><li>Supplier</li><li>News &amp; Promos</li><li>Contact Us</li>
</ul>

<div class="f-div" style="left:417px"></div>
<div class="f-title" style="left:440px">Contact Us</div>
<svg class="abs" style="left:424px;top:1085px" width="12" height="12" viewBox="0 0 12 12"><path d="M1 6 L6 1 L11 6 M3 5 V11 H9 V5" fill="none" stroke="#444" stroke-width="1.4"/></svg>
<div class="f-contact" style="left:441px;top:1084px;width:110px">Lorem ipsum dolor sit amet, consectetur adipisicing elit, sed do eiusmod tempor incididun</div>
<svg class="abs" style="left:424px;top:1116px" width="12" height="12" viewBox="0 0 12 12"><circle cx="6" cy="6" r="5.5" fill="#444"/><path d="M4 3 Q3 6 6 9 L8 8 L7 6.5 L6 7 Q5 6 5 5 L5.6 4 L4.5 3 Z" fill="#fff"/></svg>
<div class="f-contact" style="left:441px;top:1118px">+(010) - 555-01234</div>
<svg class="abs" style="left:424px;top:1134px" width="12" height="12" viewBox="0 0 12 12"><circle cx="6" cy="6" r="5.5" fill="#444"/><rect x="3" y="4" width="6" height="4" fill="none" stroke="#fff" stroke-width=".8"/><path d="M3 4 L6 6.5 L9 4" fill="none" stroke="#fff" stroke-width=".8"/></svg>
<div class="f-contact" style="left:441px;top:1136px">info@verdabio.example</div>
<svg class="abs" style="left:424px;top:1152px" width="12" height="12" viewBox="0 0 12 12"><circle cx="6" cy="6" r="5.5" fill="#444"/><circle cx="6" cy="6" r="3" fill="none" stroke="#fff" stroke-width=".8"/><path d="M3 6 H9 M6 3 V9" stroke="#fff" stroke-width=".6"/></svg>
<div class="f-contact" style="left:441px;top:1154px">www.verdabio.example</div>

<div class="f-div" style="left:557px"></div>
<div class="f-title" style="left:573px">Stay Connected With Us</div>
<div class="social" style="top:1089px"><i></i>Friendbook</div>
<div class="social" style="top:1114px"><i></i>Chirper</div>
<div class="social" style="top:1139px"><i></i>WorkLink</div>
<div class="social" style="top:1164px"><i></i>Searchly+</div>

</body>
</html>
```